Marlow Realty Real Estate Brokerage Recruiting Flyer

We are a real estate brokerage looking to hire more real estate agents. We need to list everything we have to offer as a company so real estate agents will join our company. this is our company website: www.Marlowrealty.example .

100% COMMISSION NO MONTHLY FEE
$450 Flat Transaction FEE

What We Offer:
24/7 Office Access
Free E & O Insurance for 1st Year
Free Online CE and PLE
Free 1,000 Business Cards
Free Professional Social Media Marketing
Free Printing, Scanning, and Copies
Free Buyer and Seller Presentation Packages
Free Filquay Cloud Based Document Management Access
Access to our Internal Brokerage Forum
Company Profit Sharing!
Private Offices Available to Rent

*Lead Generation Software with over 3,000 Leads
*10 Leads to Start
* Free Personal CRM and Website
*Restrictions and Rules apply

Company Address:
4817 Amberfield Road
Suite 512
Fairfax, VA 22194
Phone: 703-555-0147
email: info@marlowrealty.example

Target Market(s)

Real Estate Agents

Industry/Entity Type

Real Estate

Colors
0555a3
ffffff

Requirements
Must have
• 100% COMMISSION NO MONTHLY FEE
$450 Flat Transaction FEE

What We Offer:
24/7 Office Access
Free Online CE and PLE
Free 1,000 Business Cards
Company Profit Sharing!

*10 Leads to Start

Company Address:
4817 Amberfield Road
Suite 512
Fairfax, VA 22194
Phone: 703-555-0147

```html
<!DOCTYPE html>
<html lang="en">
<head>
<meta charset="utf-8">
<title>Marlow Realty – Agent Recruiting Flyer</title>
<link href="https://fonts.googleapis.com/css2?family=Inter:wght@300;400;600;700;800&display=swap" rel="stylesheet">
<style>
  :root {
    --brand-blue: #0a44f6;
    --brand-blue-deep: #071ded;
    --brand-blue-bright: #0b4bf7;
    --ink: #1e1e1e;
    --white: #ffffff;
    --sky: #b9f8ff;
    --sky-soft: #e4fdff;
  }
  * { margin: 0; padding: 0; box-sizing: border-box; }
  html, body { width: 927px; height: 1200px; overflow: hidden; }
  body { font-family: "Inter", "Helvetica Neue", Arial, sans-serif; color: var(--ink); }

  .flyer { position: relative; width: 927px; height: 1200px; overflow: hidden; background: var(--white); }
  .flyer > * { position: absolute; }

  .backdrop {
    inset: 0;
    background:
      radial-gradient(ellipse 520px 260px at 620px 60px, var(--sky) 0%, rgba(185,248,255,0) 100%),
      radial-gradient(ellipse 300px 200px at 80px 60px, var(--sky-soft) 0%, rgba(228,253,255,0) 100%),
      radial-gradient(ellipse 600px 160px at 460px 1200px, var(--sky) 0%, rgba(185,248,255,0) 100%),
      var(--white);
  }

  .house-band { left: 0; top: 0; width: 927px; height: 1200px; }

  .brand { left: 62px; top: 196px; display: flex; align-items: center; gap: 12px; }
  .brand-mark { width: 30px; height: 30px; background: var(--brand-blue); }
  .brand-name { font-size: 38px; font-weight: 600; color: var(--brand-blue); letter-spacing: -0.5px; }

  .headline-lead { left: 439px; top: 153px; font-size: 41px; font-weight: 300; line-height: 1; letter-spacing: -1px; white-space: nowrap; }
  .headline { left: 441px; font-size: 102px; line-height: 1; letter-spacing: -4px; white-space: nowrap; }
  .headline--real { top: 200px; font-weight: 400; }
  .headline--estate { top: 288px; font-weight: 400; }
  .headline--agents { top: 379px; left: 436px; font-weight: 700; color: var(--brand-blue); letter-spacing: -3px; }

  .offer-title { left: 62px; top: 444px; font-size: 52px; font-weight: 700; color: var(--white); line-height: 1; letter-spacing: -1px; }
  .offer-list { left: 63px; top: 501px; list-style: none; color: var(--white); font-size: 22px; line-height: 29px; white-space: nowrap; letter-spacing: -0.2px; }
  .offer-list li { position: relative; padding-left: 17px; }
  .offer-list li::before { content: ""; position: absolute; left: 0; top: 11px; width: 8px; height: 8px; border-radius: 50%; background: var(--white); }

  .rule { background: rgba(255,255,255,0.8); }
  .rule--list { left: 63px; top: 905px; width: 475px; height: 1px; }
  .rule--column { left: 581px; top: 667px; width: 1px; height: 302px; }
  .rule--deal { left: 626px; top: 829px; width: 237px; height: 1px; }

  .fine-print { left: 63px; top: 925px; color: var(--white); font-size: 17px; line-height: 23px; white-space: nowrap; letter-spacing: -0.2px; }

  .deal { color: var(--white); line-height: 1; white-space: nowrap; }
  .deal--percent { left: 634px; top: 673px; font-size: 83px; font-weight: 700; letter-spacing: -4px; }
  .deal--commission { left: 630px; top: 748px; font-size: 37px; font-weight: 700; letter-spacing: -1.5px; }
  .deal--nofee { left: 631px; top: 790px; font-size: 30px; font-weight: 400; letter-spacing: -1px; }
  .deal--dollar { left: 624px; top: 836px; font-size: 62px; font-weight: 700; }
  .deal--price { left: 662px; top: 834px; font-size: 108px; font-weight: 700; letter-spacing: -5px; }
  .deal--flat { left: 626px; top: 934px; font-size: 26px; font-weight: 400; letter-spacing: -0.6px; }

  .footer-rule { width: 1px; height: 60px; top: 1085px; background: var(--ink); }
  .footer-rule--a { left: 378px; }
  .footer-rule--b { left: 645px; }
  .contact-address, .licensing { font-size: 17.5px; line-height: 23px; white-space: nowrap; letter-spacing: -0.2px; }
  .contact-address { left: 55px; top: 1082px; }
  .licensing { left: 678px; top: 1105px; }
  .contact-phone { left: 406px; top: 1090px; font-size: 33px; font-weight: 700; color: var(--brand-blue); letter-spacing: -1.2px; line-height: 1; }
  .contact-web { left: 406px; top: 1128px; font-size: 19px; font-weight: 700; color: var(--brand-blue); letter-spacing: -0.4px; line-height: 1; white-space: nowrap; }
</style>
</head>
<body>
<main class="flyer">
  <div class="backdrop" role="img" aria-label="Soft pale cyan low-poly background pattern"></div>

  <svg class="house-band" viewBox="0 0 927 1200" aria-hidden="true">
    <defs>
      <linearGradient id="houseFill" x1="0" y1="0" x2="0" y2="1">
        <stop offset="0" stop-color="#061aec"/>
        <stop offset="1" stop-color="#0a45f6"/>
      </linearGradient>
    </defs>
    <polygon fill="var(--brand-blue-bright)" points="0,428 135,276 369,409 369,508 412,537 412,612 526,524 927,675 927,1000 714,1043 689,1001 0,1041"/>
    <polygon fill="url(#houseFill)" points="0,445 124,292 357,426 357,524 400,553 400,629 464,592 927,770 927,1000 714,1043 689,1001 0,1041"/>
  </svg>

  <div class="brand">
    <span class="brand-mark"></span>
    <span class="brand-name">Marlow Realty</span>
  </div>

  <p class="headline-lead">We are looking for more</p>
  <h1>
    <span class="headline headline--real" style="position:absolute">REAL</span>
    <span class="headline headline--estate" style="position:absolute">ESTATE</span>
    <span class="headline headline--agents" style="position:absolute">AGENTS</span>
  </h1>

  <h2 class="offer-title">We Offer:</h2>
  <ul class="offer-list">
    <li>24/7 Office Access</li>
    <li>Free E &amp; O Insurance<br>for 1st Year</li>
    <li>Free Online CE and PLE</li>
    <li>Free 1,000 Business Cards</li>
    <li>Free Professional Social Media Marketing</li>
    <li>Free Printing, Scanning, and Copies</li>
    <li>Free Buyer and Seller Presentation Packages</li>
    <li>Free Filquay Cloud Based Document<br>Management Access</li>
    <li>Access to our Internal Brokerage Forum</li>
    <li>Company Profit Sharing!</li>
    <li>Private Offices Available to Rent</li>
  </ul>

  <div class="rule rule--list"></div>
  <p class="fine-print">*Lead Generation Software with over 3,000 Leads<br>*10 Leads to Start *Free Personal CRM and Website<br>*Restrictions and Rules apply</p>

  <div class="rule rule--column"></div>
  <p class="deal deal--percent">100%</p>
  <p class="deal deal--commission">COMMISSION</p>
  <p class="deal deal--nofee">NO MONTHLY FEE</p>
  <div class="rule rule--deal"></div>
  <p class="deal deal--dollar">$</p>
  <p class="deal deal--price">450</p>
  <p class="deal deal--flat">Flat Transaction FEE</p>

  <address class="contact-address" style="font-style:normal">4817 Amberfield Road, Suite 512<br>Fairfax, VA 22194<br>email: info@marlowrealty.example</address>
  <div class="footer-rule footer-rule--a"></div>
  <p class="contact-phone">703-555-0147</p>
  <p class="contact-web">www.Marlowrealty.example</p>
  <div class="footer-rule footer-rule--b"></div>
  <p class="licensing">Licensed in D.C.,<br>Maryland, and Virginia</p>
</main>
</body>
</html>
```